Vantrel Web Services

This is a new It services company operating in Perth western Australia

we need a website that is easy to navigate without a cluttered feel to it it should have the following links and pages

About Us
Services
Clients
Contact Us
MY Vantrel (login for clients)

Hi it is a web based IT services company so we would expect customers to come to the website for 2 different purposes the first is to enquire about our services and then as they become customers come to our website to manage their services so whilst they are seperate we want do not want it to look like 2 different websites

hope this helps

Hi to update this we need a home page and templates for sub pages

this is a design brief only and not the coding of the pages or building of the site

```html
<!DOCTYPE html>
<html lang="en">
<head>
<meta charset="utf-8">
<title>Vantrel Web Services</title>
<link rel="stylesheet" href="https://fonts.googleapis.com/css2?family=Open+Sans:wght@400;600;700&display=swap">
<style>
:root{
  --red:#b3132c;
  --red-dark:#8c0d22;
  --navy:#1f2e5a;
  --ink:#333;
  --muted:#777;
  --rule:#d6d6d6;
  --bar:#1e1e1e;
  --white:#fff;
}
*{box-sizing:border-box;margin:0;padding:0}
html,body{width:796px;height:1200px;overflow:hidden}
body{font-family:"Open Sans",Arial,sans-serif;color:var(--ink);background:var(--white);position:relative}
.abs{position:absolute}

/* header */
.site-header{position:absolute;left:0;top:0;width:796px;height:53px;background:var(--white);box-shadow:0 2px 4px rgba(0,0,0,.12);z-index:2}
.brand{position:absolute;left:116px;top:6px;display:flex;align-items:center;background:var(--white);padding:6px 14px;height:46px;box-shadow:0 2px 5px rgba(0,0,0,.2)}
.brand-name{font-size:20px;font-weight:600;color:var(--ink);line-height:1}
.util-links{position:absolute;right:150px;top:5px;display:flex;gap:10px;font-size:7px;color:var(--muted);text-transform:uppercase}
.main-nav{position:absolute;left:378px;top:28px;display:flex;gap:5px}
.main-nav a{display:block;padding:4px 9px;font-size:8px;font-weight:700;color:var(--white);background:var(--red);text-decoration:none;text-transform:uppercase}
.main-nav a.is-active{background:var(--navy)}

/* hero */
.hero{position:absolute;left:0;top:53px;width:796px;height:265px;overflow:hidden}
.hero-photo{position:absolute;inset:0;background:linear-gradient(90deg,#e9e6e3 0%,#d8d2cc 30%,#8c98a8 55%,#5d6b7e 80%,#a7b0bb 100%)}
.hero-title{position:absolute;left:390px;top:108px;width:260px;font-size:23px;line-height:1.2;font-weight:400;color:var(--white)}
.hero-text{position:absolute;left:390px;top:170px;width:240px;font-size:8px;line-height:1.45;color:var(--white)}
.hero-cta{position:absolute;left:390px;top:210px;padding:8px 16px;background:var(--red);color:var(--white);font-size:10px;font-weight:700;text-transform:uppercase}
.hero-arrow{position:absolute;top:120px;width:14px;height:24px}
.hero-arrow.left{left:8px}.hero-arrow.right{right:8px}
.hero-pager{position:absolute;left:392px;top:323px;width:24px;height:6px;background:var(--bar);border-radius:2px}

/* services */
.section-title{position:absolute;width:796px;text-align:center;font-size:20px;font-weight:600;color:var(--ink)}
.section-lead{position:absolute;width:796px;text-align:center;font-size:8px;font-style:italic;color:var(--ink)}
.service{position:absolute;top:438px;width:122px}
.service-photo{height:62px;background:linear-gradient(135deg,#dfe7ef,#9eb2c6)}
.service-caption{font-size:6px;color:var(--muted);text-align:center;margin-top:6px}
.more-btn{display:block;margin:5px auto 0;width:26px;height:7px;background:var(--navy);border-radius:2px}
.rule{position:absolute;left:146px;width:512px;height:1px;background:var(--rule)}
.rule.heavy{height:2px;background:#555}

/* feed columns */
.col-title{position:absolute;top:570px;display:flex;align-items:center;gap:5px;font-size:12px;font-weight:600}
.feed{position:absolute;top:604px;width:152px}
.feed-item{display:flex;gap:6px;height:40px;border-bottom:1px solid #eee;padding-top:4px}
.feed-thumb{width:20px;height:20px;flex:none;background:#c8ced6}
.feed-text{font-size:6px;line-height:1.35;color:var(--ink)}
.feed-text b{color:var(--navy);font-weight:600}
.video{position:absolute;left:499px;top:608px;width:159px;height:108px;background:linear-gradient(135deg,#cfd6dd,#7f8b98)}
.video-caption{position:absolute;left:499px;top:722px;font-size:15px;color:var(--ink)}

/* social strip */
.tweet-icon{position:absolute;left:391px;top:894px;width:14px;height:14px;border-radius:50%;background:#3aa3d8}
.tweet-text{position:absolute;left:176px;top:918px;width:444px;text-align:center;font-size:6.5px;line-height:1.5;color:var(--muted)}

/* footer */
.site-footer{position:absolute;left:0;top:980px;width:796px;height:192px;background:var(--red-dark);color:var(--white)}
.foot-col{position:absolute;top:16px}
.foot-col h3{font-size:11px;font-weight:700;margin-bottom:8px}
.foot-col p{font-size:6.5px;line-height:1.5;width:140px}
.foot-col ul{list-style:none}
.foot-col li{font-size:6.5px;line-height:1;padding:4px 0;border-bottom:1px solid rgba(255,255,255,.25);width:130px}
.foot-btn{display:inline-block;margin-top:8px;font-size:6px;padding:2px 6px;background:var(--bar)}
.foot-map{position:absolute;left:565px;top:18px;width:93px;height:143px;background:linear-gradient(160deg,#e6e2d6,#c9d4bf)}
.bottom-bar{position:absolute;left:0;top:1172px;width:796px;height:28px;background:var(--bar);color:#bbb;font-size:6.5px}
.bottom-bar .copy{position:absolute;left:146px;top:10px}
.social{position:absolute;right:138px;top:9px;display:flex;gap:6px}
.social span{width:10px;height:10px;background:#ddd}
</style>
</head>
<body>

<header class="site-header">
  <div class="brand"><span class="brand-name">Vantrel</span></div>
  <div class="util-links"><span>MY Vantrel</span><span>Login</span><span>Search</span></div>
  <nav class="main-nav">
    <a class="is-active">Home</a><a>About Us</a><a>Services</a><a>Clients</a><a>Contact</a>
  </nav>
</header>

<section class="hero">
  <div class="hero-photo" role="img" aria-label="Photo of a smiling professional with glasses beside a colleague in an office"></div>
  <h1 class="hero-title">Lorem Ipsum Vantrel Donor Smet Sit</h1>
  <p class="hero-text">Lorem ipsum dolor sit amet, adipiscing elit sed do eiusmod tempor incididunt ut labore dolore magna.</p>
  <div class="hero-cta">Call to Action</div>
  <svg class="hero-arrow left" viewBox="0 0 14 24"><path d="M12 2 2 12l10 10" fill="none" stroke="#fff" stroke-width="3"/></svg>
  <svg class="hero-arrow right" viewBox="0 0 14 24"><path d="M2 2l10 10L2 22" fill="none" stroke="#fff" stroke-width="3"/></svg>
</section>
<div class="hero-pager abs"></div>

<h2 class="section-title" style="top:362px">Our Services</h2>
<p class="section-lead" style="top:404px">Lorem ipsum dolor sit amet, consectetur adipisicing elit, sed do eiusmod tempor incididunt ut labore et dolore</p>

<div class="service" style="left:146px"><div class="service-photo" role="img" aria-label="Photo of a business team"></div><p class="service-caption">IT Solution Lorem Ipsum Dolor Sit</p><span class="more-btn"></span></div>
<div class="service" style="left:276px"><div class="service-photo" role="img" aria-label="Photo of colleagues at a laptop"></div><p class="service-caption">Cloud Hosting Lorem Ipsum Dolor</p><span class="more-btn"></span></div>
<div class="service" style="left:406px"><div class="service-photo" role="img" aria-label="Photo of a meeting around a table"></div><p class="service-caption">Network Support Lorem Ipsum Dolor</p><span class="more-btn"></span></div>
<div class="service" style="left:536px"><div class="service-photo" role="img" aria-label="Photo of people working at computers"></div><p class="service-caption">Web Services Lorem Ipsum Dolor</p><span class="more-btn"></span></div>

<div class="rule" style="top:560px"></div>

<div class="col-title" style="left:146px"><svg width="12" height="12" viewBox="0 0 12 12"><circle cx="6" cy="6" r="5" fill="none" stroke="#333"/><path d="M3.5 6l2 2 3-4" fill="none" stroke="#333"/></svg>Latest News</div>
<div class="col-title" style="left:318px"><svg width="12" height="12" viewBox="0 0 12 12"><circle cx="6" cy="6" r="5" fill="none" stroke="#333"/><path d="M3.5 6l2 2 3-4" fill="none" stroke="#333"/></svg>From Blogs</div>
<div class="col-title" style="left:499px"><svg width="12" height="12" viewBox="0 0 12 12"><circle cx="6" cy="6" r="5" fill="none" stroke="#333"/><path d="M3.5 6l2 2 3-4" fill="none" stroke="#333"/></svg>Video</div>

<div class="feed" style="left:146px">
  <div class="feed-item"><span class="feed-thumb"></span><p class="feed-text">Lorem ipsum dolor sit amet, adipiscing sed do tempor <b>Learn More</b></p></div>
  <div class="feed-item"><span class="feed-thumb"></span><p class="feed-text">Lorem ipsum dolor sit amet, adipiscing sed do tempor <b>Learn More</b></p></div>
  <div class="feed-item"><span class="feed-thumb"></span><p class="feed-text">Lorem ipsum dolor sit amet, adipiscing sed do tempor <b>Learn More</b></p></div>
  <div class="feed-item"><span class="feed-thumb"></span><p class="feed-text">Lorem ipsum dolor sit amet, adipiscing sed do tempor <b>Learn More</b></p></div>
</div>
<div class="feed" style="left:318px">
  <div class="feed-item"><span class="feed-thumb"></span><p class="feed-text">Lorem ipsum dolor sit amet, adipiscing sed do tempor <b>Learn More</b></p></div>
  <div class="feed-item"><span class="feed-thumb"></span><p class="feed-text">Lorem ipsum dolor sit amet, adipiscing sed do tempor <b>Learn More</b></p></div>
  <div class="feed-item"><span class="feed-thumb"></span><p class="feed-text">Lorem ipsum dolor sit amet, adipiscing sed do tempor <b>Learn More</b></p></div>
  <div class="feed-item"><span class="feed-thumb"></span><p class="feed-text">Lorem ipsum dolor sit amet, adipiscing sed do tempor <b>Learn More</b></p></div>
</div>
<div class="video" role="img" aria-label="Video still of a team meeting"></div>
<p class="video-caption">Join the revolution.</p>

<span class="more-btn abs" style="left:146px;top:790px;margin:0"></span>
<span class="more-btn abs" style="left:318px;top:790px;margin:0"></span>
<span class="more-btn abs" style="left:499px;top:790px;margin:0"></span>
<div class="rule heavy" style="top:820px"></div>

<span class="tweet-icon"></span>
<p class="tweet-text">Vantrel Lorem ipsum dolor sit amet, consectetur adipisicing elit, sed do eiusmod tempor incididunt ut labore et dolore magna aliqua — http://vantrel.au · 2 hours ago · favourite · retweet</p>

<footer class="site-footer">
  <div class="foot-col" style="left:146px">
    <h3>Vantrel</h3>
    <p>Lorem ipsum dolor sit amet, consectetur adipisicing elit, sed do eiusmod tempor incididunt ut labore et dolore magna aliqua. Ut enim ad minim veniam, quis nostrud exercitation.</p>
    <span class="foot-btn">Read more</span>
  </div>
  <div class="foot-col" style="left:310px">
    <h3>Company</h3>
    <ul><li>Home</li><li>About Us</li><li>Services</li><li>How it Works</li><li>Portfolio</li><li>Contact Us</li></ul>
  </div>
  <div class="foot-col" style="left:462px;top:40px">
    <ul><li style="width:90px">Terms and conditions</li><li style="width:90px">Privacy policy</li><li style="width:90px">Sitemap</li><li style="width:90px">FAQ</li></ul>
  </div>
  <div class="foot-map" role="img" aria-label="Street map of the office location in Perth"></div>
</footer>

<div class="bottom-bar">
  <span class="copy">© 2014 Terms and Policy</span>
  <div class="social"><span></span><span></span><span></span></div>
</div>

</body>
</html>
```